Local Electrical company need some kick ass business cards

In need of some in your face design business cards for a family owned electrical service company in Edmonton, Alberta Canada. We provide reliable and trustworthy electrical service for commercial and residential work in the Edmonton and area. We have been in business for 25 years.

Target Market(s)

Residential and commercial electrical

Industry/Entity Type

Business

Contact Information for Business Card

Your welcome to change and modify the brightway electric logo. please include the lightbulb! Our Colours are black and green please stay with that.
Please include a name phone number and address on the card
phone number - 780-318-5062
#22, 418 Maple Cres, St.Albert, Alberta.
Two things that need to be on the card.
"your friendly neighborhood electrictrician"
Commercial & residential electrical repair and service

Colors
9bcb3c

Requirements
Must have
• Light bulb guy Attached
• "your friendly neighborhood electrictrician"
• Commercial & residential electrical repair and service
• phone number - 780-318-5062
• #22, 418 Maple Cres, St.Albert, Alberta.
• Our colours are black and green
Nice to have
• go wild i want something loud

```html
<!DOCTYPE html>
<html lang="en">
<head>
<meta charset="utf-8">
<title>Brightway Electric – Business Cards</title>
<link rel="stylesheet" href="https://fonts.googleapis.com/css2?family=Open+Sans:wght@400;600;700&family=Raleway:wght@300;600&display=swap">
<style>
  :root {
    --stage: #e9e6e1;
    --paper: #ffffff;
    --green-light: #8cc653;
    --green-mid: #6fa843;
    --green-deep: #1e5232;
    --green-back: #6e9d4e;
    --green-back-edge: #5f8c42;
    --ink: #222222;
    --ink-soft: #555555;
    --white: #ffffff;
    --faint: rgba(255,255,255,0.6);
  }
  * { box-sizing: border-box; margin: 0; padding: 0; }
  html, body {
    width: 1200px; height: 900px; overflow: hidden;
    background: var(--stage);
    font-family: "Open Sans", Arial, sans-serif;
  }
  .sheet {
    width: 1200px; height: 900px;
    display: flex; align-items: center; justify-content: center; gap: 40px;
  }
  .card {
    position: relative;
    width: 540px; height: 309px;
    overflow: hidden;
    box-shadow: 0 10px 28px rgba(0,0,0,0.18);
  }

  /* Front face */
  .card--front { background: var(--paper); }
  .brand {
    display: flex; align-items: center; justify-content: center; gap: 10px;
  }
  .card--front .brand {
    position: absolute; top: 36px; left: 0; right: 0;
  }
  .brand__dot {
    width: 18px; height: 18px; border-radius: 50%;
    background: var(--green-light);
  }
  .brand__name {
    font-family: "Open Sans", Arial, sans-serif;
    font-weight: 700; font-size: 22px; color: var(--ink);
    letter-spacing: 0.5px; white-space: nowrap;
  }
  .tagline {
    position: absolute; top: 74px; left: 0; right: 0;
    text-align: center;
    font-size: 12px; font-weight: 600; color: var(--ink-soft);
    letter-spacing: 0.3px;
  }
  .band {
    position: absolute; left: 0; right: 0; top: 130px; height: 96px;
    background: var(--green-light);
  }
  .band__panel {
    position: absolute; left: 0; top: 110px; width: 290px; height: 116px;
    background: var(--green-mid);
    clip-path: polygon(0 17%, 86% 0, 100% 100%, 0 100%);
  }
  .band__fold {
    position: absolute; left: 252px; top: 176px; width: 38px; height: 50px;
    background: var(--green-deep);
    clip-path: polygon(0 0, 100% 0, 100% 100%);
  }
  .person {
    position: absolute; left: 34px; top: 160px;
    color: var(--white);
    font-family: "Raleway", Arial, sans-serif;
  }
  .person__name { font-size: 24px; font-weight: 300; line-height: 1; white-space: nowrap; }
  .person__name strong { font-weight: 600; }
  .person__role { font-size: 12px; font-weight: 300; color: var(--faint); margin-top: 5px; }
  .contact {
    position: absolute; left: 312px; top: 146px;
    color: var(--white); font-size: 10px; line-height: 1.45;
  }
  .contact__block + .contact__block { margin-top: 10px; }

  /* Back face */
  .card--back {
    background: linear-gradient(160deg, var(--green-back) 0%, var(--green-back-edge) 100%);
    display: flex; flex-direction: column; align-items: center; justify-content: center; gap: 16px;
  }
  .card--back .brand { gap: 14px; }
  .card--back .brand__dot { width: 26px; height: 26px; background: var(--ink); }
  .card--back .brand__name { font-size: 34px; color: var(--white); }
  .services {
    font-size: 13px; font-weight: 600; color: var(--white);
    letter-spacing: 0.3px;
  }
</style>
</head>
<body>
<main class="sheet">
  <section class="card card--front" aria-label="Card front">
    <div class="brand">
      <span class="brand__dot"></span>
      <span class="brand__name">Brightway Electric</span>
    </div>
    <p class="tagline">Your friendly neighborhood electrician</p>
    <div class="band"></div>
    <div class="band__panel"></div>
    <div class="band__fold"></div>
    <div class="person">
      <p class="person__name">Name <strong>lastname</strong></p>
      <p class="person__role">Fonction</p>
    </div>
    <div class="contact">
      <p class="contact__block">#22, 418 Maple Cres,<br>St.Albert, Alberta.</p>
      <p class="contact__block">Phone : 780-318-5062<br>Mobile : 780-555-0143</p>
    </div>
  </section>

  <section class="card card--back" aria-label="Card back">
    <div class="brand">
      <span class="brand__dot"></span>
      <span class="brand__name">Brightway Electric</span>
    </div>
    <p class="services">Commercial &amp; residential electrical repair and service</p>
  </section>
</main>
</body>
</html>
```